Food home delivery flyer to attract new customers and drive web traffic

We need a flyer for Grubella Home Delivery for our door to door leaflet drop. The aim of our marketing is to attract new customers by driving traffic to our website and raise awareness of our service.

We want the flyer in A5, double sided, and in colour. This campaign will be primarily in print, but we need a PDF option also.

Please visit www.grubellahomedelivery.example to obtain a real feel of who we are and what we do.

The flyer should contain the Grubella Home Delivery logo, with our images to compliment our service and what we offer. All are attached to this brief, along with what wording we expect to be included in the flyer.

The main points we need to shout about are:
Sourcing fresh produce from local growers
Partnering with local businesses
Friendly team offering superior customer service
Fast, safe home delivery
Sustainable business

```html
<!DOCTYPE html>
<html lang="en">
<head>
<meta charset="utf-8">
<title>Grubella Home Delivery – A5 Flyer</title>
<link href="https://fonts.googleapis.com/css2?family=Montserrat:wght@400;500;600;700;800&display=swap" rel="stylesheet">
<style>
  :root{
    --stage:#3b3b3d;
    --forest:#1f6b2c;
    --lime:#7db544;
    --frame:#5a5a5a;
    --ink:#2e2e2e;
    --paper:#ffffff;
    --panel:rgba(255,255,255,0.86);
  }
  *{box-sizing:border-box;margin:0;padding:0}
  html,body{width:1200px;height:776px;overflow:hidden;background:var(--stage);font-family:"Montserrat",sans-serif;color:var(--ink)}
  .flyer{position:absolute;top:48px;width:481px;height:680px;background:var(--paper);overflow:hidden}
  .flyer--front{left:90px}
  .flyer--back{left:629px}

  /* front */
  .front__header{position:absolute;left:0;top:0;width:100%;height:96px;background:var(--forest);display:flex;align-items:center;justify-content:center;text-align:center}
  .front__headline{color:#fff;font-weight:800;font-size:22px;line-height:1.2;letter-spacing:1px;text-transform:uppercase}
  .front__grid{position:absolute;left:0;top:96px;width:100%;height:422px;background:var(--lime)}
  .photo{position:absolute;border:3px solid var(--frame)}
  .photo--pizza{left:12px;top:12px;width:258px;height:112px;background:linear-gradient(135deg,#b4482a,#d9823e 55%,#8a3a1f)}
  .photo--platter{left:278px;top:12px;width:191px;height:176px;background:linear-gradient(160deg,#f1ece4,#e6c9b4 50%,#c94a35)}
  .photo--produce{left:12px;top:272px;width:296px;height:138px;background:linear-gradient(120deg,#6e3a6b,#d8572c 35%,#e5b53a 55%,#5f9a3a 80%,#3c6c2c)}
  .photo--bakes{left:316px;top:196px;width:153px;height:214px;background:linear-gradient(170deg,#c9a770,#8aa84a 55%,#c67a3a)}
  .front__logo{position:absolute;left:12px;top:132px;width:258px;height:132px;background:var(--paper);border:3px solid var(--frame);display:flex;align-items:center;justify-content:center}
  .brand{display:flex;align-items:center;gap:10px;color:var(--forest);font-weight:700;text-align:center;line-height:1.1}
  .brand__dot{width:14px;height:14px;border-radius:50%;background:var(--lime);flex:none}
  .brand__name{font-size:24px}
  .front__footer,.back__footer{position:absolute;left:0;width:100%;text-align:center;font-size:13.5px;line-height:1.45}
  .front__footer{top:548px}
  .back__footer{top:588px}
  .em{color:var(--forest);font-weight:700}

  /* back */
  .back__logo{position:absolute;left:0;top:0;width:100%;height:120px;display:flex;align-items:center;justify-content:center}
  .back__logo .brand__name{font-size:28px}
  .back__scene{position:absolute;left:0;top:124px;width:100%;height:446px;background:linear-gradient(100deg,#5a3a6a,#c5623a 25%,#e8c24a 50%,#c4d66a 72%,#a33a3a)}
  .back__panel{position:absolute;left:28px;top:14px;width:425px;height:416px;background:var(--panel);border:3px solid var(--frame);padding:20px 26px 0;text-align:center;overflow:hidden}
  .back__title{color:var(--forest);font-weight:800;font-size:17px;letter-spacing:.5px;text-transform:uppercase;margin-bottom:12px}
  .back__copy{font-size:10.6px;line-height:1.45;margin-bottom:11px}
  .offer{position:absolute;left:50%;bottom:0;transform:translateX(-50%);width:340px;height:56px;background:var(--forest);border-radius:40px 40px 0 0;color:#fff;font-size:12px;line-height:1.4;display:flex;flex-direction:column;align-items:center;justify-content:center}
  .offer strong{font-weight:700}
</style>
</head>
<body>

<article class="flyer flyer--front">
  <header class="front__header">
    <h1 class="front__headline">Sourcing fresh produce<br>from local growers</h1>
  </header>
  <section class="front__grid">
    <div class="photo photo--pizza" role="img" aria-label="Tomato and basil pizza"></div>
    <div class="photo photo--platter" role="img" aria-label="Platter of bruschetta, olives, chillies and cured meats"></div>
    <div class="front__logo">
      <div class="brand"><span class="brand__dot"></span><span class="brand__name">Grubella<br>Home Delivery</span></div>
    </div>
    <div class="photo photo--produce" role="img" aria-label="Colourful spread of fresh vegetables and fruit"></div>
    <div class="photo photo--bakes" role="img" aria-label="Tray of flatbreads, falafel, scotch eggs and roasted vegetables"></div>
  </section>
  <footer class="front__footer">
    Shop now at <span class="em">www.grubellahomedelivery.example</span><br>
    or call one of our friendly team at the farm on <span class="em">01632 960418.</span><br>
    Start enjoying food wit provenance now.
  </footer>
</article>

<article class="flyer flyer--back">
  <header class="back__logo">
    <div class="brand"><span class="brand__dot"></span><span class="brand__name">Grubella Home Delivery</span></div>
  </header>
  <section class="back__scene" role="img" aria-label="Background of assorted fresh fruit and vegetables">
    <div class="back__panel">
      <h2 class="back__title">Fast, safe home delivery</h2>
      <p class="back__copy">Lovingly picked Kentish food safely delivered from our farm to your home by passionate local people who care.</p>
      <p class="back__copy">Avoid the supermarkets and enjoy a unique and balanced food experience with provenance. Order online at <span class="em">www.grubellahomedelivery.example</span> for fast contactless next day delivery.</p>
      <p class="back__copy">Grubella brings you the very best producers and growers from The Garden of England to deliver you a delicious choice for all your dining needs. From fresh produce boxes, handmade picnic boxes, fresh Kentish berry boxes to the finest local beer and wines–we've got it covered.</p>
      <p class="back__copy">Using environmentally consciouspractices and minimal packaging, working hand in hand with reduced food miles brings you peace of mind with our efforts for a sustainable future.</p>
      <div class="offer">
        <span>Enjoy <strong>25%</strong> off all your orders in <strong>July</strong></span>
        <span>enter code <strong>LOCALFRESH</strong> at the checkout</span>
      </div>
    </div>
  </section>
  <footer class="back__footer">
    Shop now at <span class="em">www.grubellahomedelivery.example</span><br>
    or call one of our friendly team at the farm on <span class="em">01632 960418.</span><br>
    Start enjoying food wit provenance now.
  </footer>
</article>

</body>
</html>
```